Design a Professional Stationery

Hi everyone,
I would like to make a design of stationery for my company Corvel Wrap (www.corvelwrap-example.com).
General Info: We are manufacturers of packaging supplies (poly bubble mailers, kraft bubble mailers, bubble wrap, tape, stretch film). We have couple of big warehouses in Los Angeles and New Jersey that serves East and West Coasts. We store lot of boxes with our product. We are wholesalers so we work with big serious distributors.

Project Goals: Create a business stationery that will look professional, modern and straight to the point. Colors: Dark blue, white, light blue (please see the web site). Blue is the color of success.
I want them to be presentable. As you might need to imagine my team will walk around the businesses and leave folders with information at clients table. We will distribute them at the trade shows, business meetings etc.

Target Market(s)

Business professionals looking for professional wholesaler manufacturer.

Industry/Entity Type

It Company

Font styles to use
Serif
Sans Serif

Colors
3276b5
0255a3
85acd3
cedeed
eaf1f7

Requirements
Must have
• People photos, product photos, add professional warehouse photos, truck, machinery.
Nice to have
• NLP
Should not have
• Use your imagination, no limits so far

```html
<!DOCTYPE html>
<html lang="en">
<head>
<meta charset="utf-8">
<title>Corvel Wrap – Business Card</title>
<link rel="stylesheet" href="https://fonts.googleapis.com/css2?family=Questrial&family=Mulish:wght@700&display=swap">
<style>
  :root {
    --backdrop: #1d1e21;
    --navy: #0c2a5c;
    --navy-deep: #0a2454;
    --brand-blue: #2f6db0;
    --strip-blue: #3a6fae;
    --paper: #f7f7f7;
    --ink: #23324a;
    --icon-grey: #c9d3e2;
    --white: #ffffff;
  }
  * { margin: 0; padding: 0; box-sizing: border-box; }
  html, body { width: 1200px; height: 1000px; overflow: hidden; }
  body {
    background: var(--backdrop);
    font-family: "Questrial", "Century Gothic", sans-serif;
    position: relative;
  }
  .card {
    position: absolute;
    width: 580px;
    height: 324px;
    overflow: hidden;
  }
  .card--front { left: 200px; top: 148px; background: var(--paper); }
  .card--back  { left: 420px; top: 548px; background: var(--navy); }

  .front-band {
    position: absolute; left: 0; top: 165px; width: 100%; height: 123px;
    background: var(--navy);
  }
  .front-strip {
    position: absolute; left: 0; top: 288px; width: 100%; height: 36px;
    background: var(--strip-blue);
  }
  .band-notch { position: absolute; left: 32px; top: 165px; }

  .holder { position: absolute; left: 36px; top: 83px; }
  .holder-name {
    font-family: "Mulish", "Century Gothic", sans-serif;
    font-weight: 700; font-size: 19px; letter-spacing: 0.5px;
    color: var(--brand-blue);
  }
  .holder-role { font-size: 15px; color: var(--ink); margin-top: 2px; }

  .brand { position: absolute; display: flex; align-items: center; }
  .brand-name {
    font-family: "Questrial", "Century Gothic", sans-serif;
    text-transform: uppercase; letter-spacing: 1px; line-height: 1;
  }
  .brand-square { display: block; margin-left: 12px; }
  .card--front .brand { right: 35px; top: 78px; }
  .card--front .brand-name { font-size: 30px; color: var(--navy); }
  .card--front .brand-square { width: 18px; height: 18px; background: var(--navy); }
  .card--back .brand { left: 0; right: 0; top: 142px; justify-content: center; }
  .card--back .brand-name { font-size: 40px; color: var(--white); }
  .card--back .brand-square { width: 22px; height: 22px; background: var(--white); }

  .contact-list {
    position: absolute; left: 36px; top: 200px; list-style: none;
    color: var(--white); font-size: 14px;
  }
  .contact-list li { display: flex; align-items: center; height: 18px; }
  .contact-list svg { width: 13px; height: 13px; margin-right: 9px; flex: none; }
  .address {
    position: absolute; right: 34px; top: 200px; text-align: right;
    color: var(--white); font-size: 14px; line-height: 18px; font-style: normal;
  }
</style>
</head>
<body>
  <section class="card card--front" aria-label="Business card front">
    <div class="front-band"></div>
    <div class="front-strip"></div>
    <svg class="band-notch" width="24" height="16" viewBox="0 0 24 16" aria-hidden="true">
      <polygon points="0,0 24,0 12,16" fill="#f7f7f7"/>
    </svg>

    <div class="holder">
      <p class="holder-name">MARIN OSTROV</p>
      <p class="holder-role">General Manager</p>
    </div>

    <div class="brand">
      <span class="brand-name">Corvel Wrap</span>
      <span class="brand-square"></span>
    </div>

    <ul class="contact-list">
      <li>
        <svg viewBox="0 0 13 13" aria-hidden="true"><rect width="13" height="13" rx="2" fill="#c9d3e2"/><path d="M4 3 L5.5 3 L6 5 L5 5.8 Q5.8 7.6 7.2 8 L8 7 L10 7.5 L10 9 Q6 10 3.5 4.5 Z" fill="#0c2a5c"/></svg>
        555-014-2290
      </li>
      <li>
        <svg viewBox="0 0 13 13" aria-hidden="true"><rect width="13" height="13" rx="2" fill="#c9d3e2"/><rect x="2.5" y="4" width="8" height="5.5" fill="none" stroke="#0c2a5c" stroke-width="1"/><path d="M2.5 4 L6.5 7 L10.5 4" fill="none" stroke="#0c2a5c" stroke-width="1"/></svg>
        info@corvelwrap-example.com
      </li>
      <li>
        <svg viewBox="0 0 13 13" aria-hidden="true"><rect width="13" height="13" rx="2" fill="#c9d3e2"/><circle cx="6.5" cy="6.5" r="4" fill="none" stroke="#0c2a5c" stroke-width="1"/><ellipse cx="6.5" cy="6.5" rx="1.8" ry="4" fill="none" stroke="#0c2a5c" stroke-width="0.8"/><line x1="2.5" y1="6.5" x2="10.5" y2="6.5" stroke="#0c2a5c" stroke-width="0.8"/></svg>
        www.corvelwrap-example.com
      </li>
    </ul>

    <address class="address">4200 Harbor Row<br>Lakeview CA 90000</address>
  </section>

  <section class="card card--back" aria-label="Business card back">
    <div class="brand">
      <span class="brand-name">Corvel Wrap</span>
      <span class="brand-square"></span>
    </div>
  </section>
</body>
</html>
```